Vascular Secialist needs a tri-fold brochure

I would like to create a tri- fold of all the services that the vascular practice offers. The practice specializes in lower extremity vascular diseases. I would like to have the tri-fold have brief descriptions of all the services as well as images of the practice to show case the top of the line technology. The trip-fold will be front in back with a crisp modern design. The diseases that they treat are: arterial disease, venous disease, varicose veins, chronic venous insufficiency, deep vein thrombosis, uterine fibroids, pelvic and labial varicose veins, varicocele. Treatment options for all diseases that the practice treats.

Target Market(s)

Doctors

Industry/Entity Type

Medical

Font styles to use
Other font styles liked:
• Myriod Pro SemiExtende

Colors
33a6d7
86cae7
aaaaaa
85cae6
dcedf6
cee9f5
757575
9d9d9d
c3c3c3

Requirements
Must have
• creativity and taglines that capture the reader
Nice to have
• I would like the piece to mirror the website. www.larvinmesaclinic.com

```html
<!DOCTYPE html>
<html lang="en">
<head>
<meta charset="utf-8">
<title>Larvin Mesa Vein Clinic – Tri-fold Brochure</title>
<link rel="stylesheet" href="https://fonts.googleapis.com/css2?family=Encode+Sans+Condensed:wght@300;400;600&family=Open+Sans:wght@400;600&display=swap">
<style>
  :root{
    --blue:#33a6d7;
    --blue-light:#86cae7;
    --blue-pale:#cee9f5;
    --blue-mist:#dcedf6;
    --grey-panel:#e9e9e9;
    --grey-text:#757575;
    --grey-mid:#9d9d9d;
    --ink:#3c3c3c;
    --white:#ffffff;
    --red:#c8202a;
    --bg:#d9d9d9;
  }
  *{box-sizing:border-box;margin:0;padding:0}
  html,body{width:1200px;height:873px;overflow:hidden;background:var(--bg)}
  body{font-family:"Open Sans",sans-serif;color:var(--ink);position:relative}
  .panel{position:absolute;top:36px;width:280px;height:800px;overflow:hidden}
  .panel--diseases{left:20px;background:var(--white)}
  .panel--pelvic{left:300px;background:var(--blue-pale)}
  .panel--team{left:580px;background:var(--grey-panel)}
  .panel--cover{left:900px;background:var(--white)}

  .photo{display:block;width:100%}
  .photo--lobby{height:232px;background:linear-gradient(135deg,#9fb7c4 0%,#e6e2dc 45%,#c9b9a6 100%);position:relative}
  .lobby-name{position:absolute;right:14px;bottom:14px;display:flex;align-items:center;gap:6px;font-family:"Encode Sans Condensed",sans-serif;font-weight:400;font-size:15px;letter-spacing:.5px;color:#4a4a4a}
  .lobby-name .dot{width:9px;height:9px;border-radius:50%;background:#4a4a4a}

  .diseases-body{padding:26px 20px 0 22px;font-family:"Encode Sans Condensed",sans-serif}
  .diseases-title{font-weight:300;font-size:30px;color:var(--blue);letter-spacing:.3px;margin-bottom:10px}
  .diseases-body h3{font-weight:600;font-size:10.5px;color:var(--ink);margin:14px 0 10px}
  .diseases-body h3:first-of-type{margin-top:0}
  .diseases-body p{font-weight:300;font-size:10.2px;line-height:15px;color:var(--ink)}

  .copy{padding:0 22px;font-size:9.3px;line-height:12.6px}
  .copy h3{font-weight:600;font-size:9.8px;margin:14px 0 10px;color:var(--ink)}
  .copy h3 .tag{font-weight:400;color:var(--blue)}
  .copy p + p{margin-top:8px}
  .panel--pelvic .copy{padding-top:38px}
  .panel--pelvic .copy h3:first-child{margin-top:0}

  .photo--doctors{height:316px;display:flex;gap:2px;background:var(--white)}
  .doctor{flex:1;position:relative;background:linear-gradient(180deg,#cfdcd2 0%,#a9b9c6 40%,#4f5d9a 100%)}
  .doctor-name{position:absolute;bottom:6px;left:0;right:0;text-align:center;font-size:6.5px;color:var(--white)}
  .panel--team .copy{padding-top:30px}

  .cover-brand{height:180px;display:flex;align-items:center;justify-content:center;gap:12px}
  .cover-brand .mark{width:22px;height:22px;border-radius:50%;background:#3a2a22}
  .cover-brand .name{font-family:"Encode Sans Condensed",sans-serif;font-weight:400;color:#3a2a22;line-height:1}
  .cover-brand .name b{display:block;font-weight:400;font-size:34px;letter-spacing:1px}
  .cover-brand .name span{display:block;font-size:11px;letter-spacing:5px;margin-top:4px}
  .cover-photo{position:absolute;left:20px;right:20px;top:180px;height:570px;background:linear-gradient(180deg,#7fc3e3 0%,var(--blue) 55%,#2f8fc0 100%)}
  .cover-tagline{position:absolute;left:40px;bottom:40px;font-family:"Encode Sans Condensed",sans-serif;font-weight:300;font-size:30px;line-height:34px;color:var(--white);letter-spacing:1px}
  .cover-url{position:absolute;bottom:18px;left:0;right:0;text-align:center;font-size:9px;color:var(--blue)}
</style>
</head>
<body>

<section class="panel panel--diseases">
  <div class="photo photo--lobby" role="img" aria-label="Photo of the bright clinic lobby with curved windows and lounge seating">
    <div class="lobby-name"><span class="dot"></span>LARVIN MESA</div>
  </div>
  <div class="diseases-body">
    <h2 class="diseases-title">DISEASES WE TREAT</h2>
    <h3>Peripheral Arterial Disease</h3>
    <p>Peripheral Arterial Disease (PAD) develops when the arteries in the legs build up plaque, obstructing and narrowing the arteries and preventing blood, oxygen, glucose from flowing properly to tissue. This lack of blood-flow causes pain, cramping, and swelling in the legs as the muscles and tissue starve for blood and if untreated, can lead to amputation of the toes and/or foot.</p>
    <h3>Varicose Veins</h3>
    <p>Closely related to chronic venous insufficiency, varicose veins are enlarged veins that are visible through the skin. The veins often appear bulging or twisted and are generally larger than three millimeters in diameter. Varicose veins affect one out of two people over the age of 50, and women who have had children are particularly susceptible.</p>
    <h3>Deep Venous Thrombosis</h3>
    <p>A DVT is the formation of a blood clot (thrombus) in a deep veins, most commonly occurring in the legs. This thrombus disrupts the normal flow of blood from the legs or arms back to the heart. A DVT presents a serious risk to your life; the clot could move to your heart or lungs causing serious and sometimes fatal conditions. You must see a doctor immediately if you think you may have a DVT.</p>
  </div>
</section>

<section class="panel panel--pelvic">
  <div class="copy">
    <h3>Varicocele <span class="tag">A male condition</span></h3>
    <p>A varicocele (VAR-ih-koe-seel) is an enlargement of the veins within the scrotum. A varicocele is similar to a varicose vein that can occur in the legs or in the female pelvic area. 15% of the general male population suffer from varicocele with more than 80% occurring on the left side and the remainder on both sides. They are generally acquired during puberty.</p>
    <p>Most varicoceles are asymptomatic; however, some can cause scrotal pain. This pain is generally mild to moderate, occurs with long periods of sitting, standing or activity and is relieved by lying down. Although it can be uncomfortable before bedtime (after a long day of activity), it generally does not occur upon awakening after a night's rest. The pain is dull, congestive, "tooth ache" like and generally doesn't refer elsewhere. The resulting backup causes the veins to widen (dilate) which can lead to damage to the testicle and result in worsened fertility. Our physicians can provide targeted treatment for varicocele called "varicocele repair."</p>
    <h3>Pelvic Venous Congestion (PVCS)</h3>
    <p>Pelvic venous congestion syndrome (PVCS) also known as ovarian vein reflux, causes chronic pelvic pain in approximately 13-40% of women. The ovarian veins carry venous blood from the ovaries and pelvis up to the level of the renal veins in the abdomen. All veins have valves to help guide blood flow back up towards the heart. When these valves become damaged or dysfunctional, some blood flows backwards causing the veins to become engorged or "congested," leading to varicose veins. PVCS is essentially varicose veins in the pelvis due to venous insufficiency in the ovarian veins. These internal varicose veins can cause chronic, debilitating pain. This pressure may also cause visible varicose veins around the vulva, vagina, inner thigh, sometimes the buttocks, and down the leg(s).</p>
    <h3>Pelvic and Labial Varicose Veins</h3>
    <p>Pelvic venous congestion syndrome may be accompanied by varicose veins and labial varicose veins. It is a form of venous insufficiency by which women's pelvic veins become enlarged and dilated during pregnancy and may continue after the baby has been born. Symptoms often worsen with each pregnancy and can include frequent or continuous pain that is most prominent during pregnancy and after long periods of standing.</p>
  </div>
</section>

<section class="panel panel--team">
  <div class="photo photo--doctors">
    <div class="doctor" role="img" aria-label="Portrait of a physician in blue scrubs with arms crossed">
      <span class="doctor-name">Daniel R. Ostrow, MD</span>
    </div>
    <div class="doctor" role="img" aria-label="Portrait of a second physician in blue scrubs with arms crossed">
      <span class="doctor-name">Marcus Elling, MD</span>
    </div>
  </div>
  <div class="copy">
    <p>Labial varicose veins may be due to iliac vein obstruction from compression or old clots, or they may be due to ovarian vein reflux with pelvic venous insufficiency. In some patients, the primary problem is reflux (abnormal reversal of flow) in the veins of the deep pelvis through veins near the vagina into the labia and surrounding tissues. Like with all types of venous reflux disease, our physicians provided targeted treatments that divert blood flow through healthy veins and eliminate discomfort.</p>
    <h3>Uterine Fibroids</h3>
    <p>Uterine fibroids (fibroid tumors, leiomyomas, or myomas) are benign masses that grow on the outside or in the muscle wall of the uterus. Fibroids are very common in women in their 30s and 40s— as many 70%-80% of all women will have fibroids by age 50. While the cause of Fibroids is not conclusively proven, they seem to be linked to estrogen levels and family history. Symptoms can include heavy bleeding, pelvic pressure, frequent urination and back pain. Our physicians offer uterine fibroid embolization, a minimally invasive treatment that shrinks fibroids without surgery and with a short recovery.</p>
  </div>
</section>

<section class="panel panel--cover">
  <div class="cover-brand">
    <span class="mark"></span>
    <div class="name"><b>LARVIN MESA</b><span>VEIN CLINIC</span></div>
  </div>
  <div class="cover-photo" role="img" aria-label="Blue-toned photo of the clinic building overlaid with large red script lettering of the word life">
    <p class="cover-tagline">OUR GOAL<br>IMPROVE YOUR<br>QUALITY OF</p>
  </div>
  <p class="cover-url">www.larvinmesaclinic.com</p>
</section>

</body>
</html>
```